Letterhead, business cards, envelopes
Thornwell Holdings Property Management
Creative Brief
Professional
Dean Pultorak
Real Estate Asset Manager
27816 Brisbane Ave., Los Alamitos Ca 90720
dean@thpropertymgmt.example
www.thpropertymgmt.example
designers choice

```html
<!DOCTYPE html>
<html lang="en">
<head>
<meta charset="utf-8">
<title>Thornwell Holdings Property Management – Stationery</title>
<link rel="stylesheet" href="https://fonts.googleapis.com/css2?family=Cinzel:wght@400&family=Open+Sans:wght@400;600&display=swap">
<style>
  :root {
    --bg: #e9e6e2;
    --paper: #ffffff;
    --ink: #2f3a3c;
    --slate: #4d6166;
    --steel: #6f8488;
    --muted: #8a8f91;
    --black-card: #111314;
  }
  * { box-sizing: border-box; margin: 0; padding: 0; }
  html, body { width: 1200px; height: 1020px; overflow: hidden; }
  body {
    background: var(--bg);
    font-family: "Open Sans", Arial, sans-serif;
    color: var(--ink);
    position: relative;
  }
  .sheet, .card {
    position: absolute;
    background: var(--paper);
    box-shadow: 0 6px 18px rgba(0,0,0,.18);
    overflow: hidden;
  }

  /* Brand lockup: plain square + name in one colour and weight */
  .brand { display: flex; align-items: center; gap: 8px; }
  .brand-mark { background: var(--slate); flex: none; }
  .brand-name {
    font-family: "Cinzel", Georgia, serif;
    font-weight: 400;
    color: var(--slate);
    line-height: 1.05;
    text-transform: uppercase;
    white-space: nowrap;
  }
  .tagline {
    font-size: 6px;
    letter-spacing: .12em;
    text-transform: uppercase;
    color: var(--muted);
    white-space: nowrap;
  }

  /* Business card – front */
  .card-front { left: 130px; top: 245px; width: 250px; height: 125px; }
  .card-front .brand { position: absolute; left: 18px; top: 12px; gap: 6px; }
  .card-front .brand-mark { width: 26px; height: 26px; }
  .card-front .brand-name { font-size: 9px; }
  .holder { position: absolute; right: 14px; top: 56px; text-align: center; width: 120px; }
  .holder-name { font-size: 10px; font-weight: 600; color: var(--ink); }
  .holder-title { font-size: 5.5px; color: var(--muted); margin-top: 1px; }
  .card-rule { position: absolute; left: 0; right: 0; top: 84px; height: 3px; display: flex; }
  .card-rule .dark { width: 34px; background: var(--ink); }
  .card-rule .gap { width: 3px; }
  .card-rule .steel { flex: 1; background: var(--steel); }
  .card-contact { position: absolute; top: 92px; font-size: 5px; line-height: 1.7; color: var(--muted); white-space: nowrap; }
  .card-contact.address { left: 10px; }
  .card-contact.phones { left: 92px; }
  .card-contact.web { left: 150px; }
  .icon { display: inline-block; width: 4px; height: 4px; background: var(--slate); margin-right: 4px; vertical-align: middle; }

  /* Business card – backs */
  .card-back-light { left: 130px; top: 392px; width: 250px; height: 125px; }
  .card-back-dark { left: 130px; top: 539px; width: 250px; height: 125px; background: var(--black-card); }
  .card-back-light .brand, .card-back-dark .brand {
    position: absolute; left: 50%; top: 24px; transform: translateX(-50%);
    flex-direction: column; gap: 6px; text-align: center;
  }
  .card-back-light .brand-mark, .card-back-dark .brand-mark { width: 38px; height: 38px; }
  .card-back-light .brand-name, .card-back-dark .brand-name { font-size: 9px; }
  .card-back-dark .brand-mark { background: var(--steel); }
  .card-back-dark .brand-name { color: #c8d0d2; }
  .card-web { position: absolute; left: 0; right: 0; bottom: 16px; text-align: center; font-size: 5.5px; color: var(--muted); }
  .card-back-dark .card-web { color: #9aa4a6; }

  /* Letterhead */
  .letterhead { left: 450px; top: 125px; width: 610px; height: 790px; }
  .letterhead .brand { position: absolute; left: 40px; top: 40px; gap: 10px; }
  .letterhead .brand-mark { width: 58px; height: 58px; }
  .letterhead .brand-name { font-size: 18px; }
  .letterhead .tagline { margin-top: 4px; font-family: "Open Sans", Arial, sans-serif; font-size: 7px; }
  .lh-rule { position: absolute; left: 0; right: 0; top: 722px; height: 6px; display: flex; }
  .lh-rule .dark { width: 50px; background: var(--ink); }
  .lh-rule .gap { width: 6px; }
  .lh-rule .steel { flex: 1; background: var(--steel); }
  .lh-footer { position: absolute; top: 740px; font-size: 7.5px; line-height: 1.7; color: var(--muted); white-space: nowrap; }
  .lh-footer.address { left: 58px; }
  .lh-footer.phones { left: 160px; }
  .lh-footer.web { left: 244px; }
</style>
</head>
<body>

  <section class="card card-front" aria-label="Business card front">
    <div class="brand">
      <span class="brand-mark"></span>
      <span class="brand-name">Thornwell Holdings<br>Property Management</span>
    </div>
    <div class="holder">
      <div class="holder-name">Dean Pultorak</div>
      <div class="holder-title">Real Estate Asset Manager</div>
    </div>
    <div class="card-rule"><span class="dark"></span><span class="gap"></span><span class="steel"></span></div>
    <div class="card-contact address">27816 Brisbane Ave.,<br>Los Alamitos Ca 90720</div>
    <div class="card-contact phones">
      <div><span class="icon"></span>714 555 0142</div>
      <div><span class="icon"></span>714 555 0178</div>
    </div>
    <div class="card-contact web">
      <div><span class="icon"></span>dean@thpropertymgmt.example</div>
      <div><span class="icon"></span>www.thpropertymgmt.example</div>
    </div>
  </section>

  <section class="card card-back-light" aria-label="Business card back, light">
    <div class="brand">
      <span class="brand-mark"></span>
      <span class="brand-name">Thornwell Holdings</span>
    </div>
    <div class="card-web">www.thpropertymgmt.example</div>
  </section>

  <section class="card card-back-dark" aria-label="Business card back, dark">
    <div class="brand">
      <span class="brand-mark"></span>
      <span class="brand-name">Thornwell Holdings</span>
    </div>
    <div class="card-web">www.thpropertymgmt.example</div>
  </section>

  <section class="sheet letterhead" aria-label="Letterhead">
    <div class="brand">
      <span class="brand-mark"></span>
      <div>
        <div class="brand-name">Thornwell Holdings<br>Property Management</div>
        <div class="tagline">Residential · Multifamily · Commercial</div>
      </div>
    </div>
    <div class="lh-rule"><span class="dark"></span><span class="gap"></span><span class="steel"></span></div>
    <div class="lh-footer address">27816 Brisbane Ave.,<br>Los Alamitos Ca 90720</div>
    <div class="lh-footer phones">
      <div><span class="icon"></span>714 555 0142</div>
      <div><span class="icon"></span>714 555 0178</div>
    </div>
    <div class="lh-footer web">
      <div><span class="icon"></span>dean@thpropertymgmt.example</div>
      <div><span class="icon"></span>www.thpropertymgmt.example</div>
    </div>
  </section>

</body>
</html>
```